General Contractors need a new Crisp updated Card Design

We need a new business card design for our company of 25 years based in Toronto call Pollvarn Building Inc. : Our goal is to be the leading commercial contractors in Toronto by providing exceptional value to our clients. We work very hard to deliver professional, quality, service in conjunction with consistent price competitiveness to all of our clients on every single project.

Target Market(s)

Design & Build Clients

Industry/Entity Type

Construction Company

Contact Information for Business Card

Address:
18 West Marlow Field Road, Unit 17, Dunmore Vale, ON, K7T 2M9
Office: 905-218-6937

Pollvarns Logo
Employee Job Description
Employee Cell Phone #
Employee Email
www.pollvarn.example

Colors

Designer to choose colors to be used in the design.

Requirements
Must have
• Quote Company Saying:
• "Professional. Quality. Service."
Nice to have
• New Crisp up to date look. simple & fresh ( Not to Busy)
Should not have
• NO BLUE PRINTS ON THE BUSINESS CARDS

```html
<!DOCTYPE html>
<html lang="en">
<head>
<meta charset="utf-8">
<title>Pollvarn Building Inc. — Business Card</title>
<link rel="stylesheet" href="https://fonts.googleapis.com/css2?family=Libre+Baskerville:wght@400;700&family=Lato:wght@400&display=swap">
<style>
  :root {
    --teal: #006b63;
    --teal-line: #5f9e97;
    --sage: #b4c8bd;
    --white: #ffffff;
    --stage: #1d1e20;
    --serif: "Libre Baskerville", Georgia, serif;
    --sans: "Lato", Arial, sans-serif;
  }
  * { box-sizing: border-box; margin: 0; padding: 0; }
  html, body {
    width: 1200px; height: 960px; overflow: hidden;
    background: var(--stage);
  }
  .canvas { position: relative; width: 1200px; height: 960px; }
  .card {
    position: absolute; left: 250px; width: 700px; height: 400px;
    overflow: hidden;
  }

  /* Back of card */
  .card-back {
    top: 60px; background: var(--teal);
    display: flex; flex-direction: column; align-items: center; justify-content: center;
  }
  .back-brand { display: flex; align-items: center; gap: 22px; }
  .brand-square { width: 110px; height: 110px; background: var(--white); flex: none; }
  .back-name {
    font-family: var(--serif); font-weight: 700; font-size: 40px;
    color: var(--white); letter-spacing: 1px; line-height: 1.1;
    text-transform: uppercase;
  }
  .back-url {
    margin-top: 34px;
    font-family: var(--sans); font-size: 20px; letter-spacing: 3px;
    color: var(--white);
  }
  .tagline {
    margin-top: 14px;
    font-family: var(--serif); font-size: 15px; letter-spacing: 2px;
    color: var(--sage);
  }

  /* Front of card */
  .card-front { top: 500px; background: var(--white); }
  .front-brand {
    position: absolute; top: 44px; left: 0; width: 100%;
    display: flex; align-items: center; justify-content: center; gap: 16px;
  }
  .front-brand .brand-square { width: 64px; height: 64px; background: var(--teal); }
  .front-name {
    font-family: var(--serif); font-weight: 700; font-size: 28px; line-height: 1.1;
    color: var(--teal); text-transform: uppercase; letter-spacing: 1px;
  }
  .person {
    position: absolute; top: 140px; left: 0; width: 100%;
    text-align: center; font-family: var(--serif); color: var(--teal);
  }
  .person-name { font-weight: 700; font-size: 18px; letter-spacing: 1px; }
  .person-title { font-weight: 400; font-size: 16px; letter-spacing: 1px; margin-top: 2px; }
  .contact-band {
    position: absolute; left: 0; bottom: 0; width: 100%; height: 170px;
    background: var(--teal); color: var(--white);
    display: flex; align-items: center; justify-content: center;
    font-family: var(--sans);
  }
  .address {
    width: 280px; text-align: right; font-size: 16px; line-height: 1.45;
    padding-right: 22px; font-style: normal;
  }
  .divider { width: 1px; height: 110px; background: var(--teal-line); }
  .contacts {
    list-style: none; width: 280px; padding-left: 22px;
    font-size: 16px; line-height: 1.5;
  }
  .contacts li { display: flex; align-items: center; gap: 8px; }
  .contacts svg { width: 14px; height: 14px; flex: none; fill: var(--white); }
</style>
</head>
<body>
<main class="canvas">

  <section class="card card-back" aria-label="Business card, back">
    <div class="back-brand">
      <div class="brand-square"></div>
      <div class="back-name">Pollvarn<br>Building Inc.</div>
    </div>
    <div class="back-url">www.pollvarn.example</div>
    <div class="tagline">Professional. Quality. Service.</div>
  </section>

  <section class="card card-front" aria-label="Business card, front">
    <div class="front-brand">
      <div class="brand-square"></div>
      <div class="front-name">Pollvarn<br>Building Inc.</div>
    </div>

    <div class="person">
      <div class="person-name">DANIEL ASHCROFT</div>
      <div class="person-title">PRESIDENT</div>
    </div>

    <div class="contact-band">
      <address class="address">
        18 West Marlow Field Road<br>
        Unit 17, Dunmore Vale<br>
        ON, K7T 2M9
      </address>
      <div class="divider"></div>
      <ul class="contacts">
        <li>
          <svg viewBox="0 0 16 16" aria-hidden="true"><path d="M3.2 1.5l2.3 2.6-1.3 1.7c.9 2 2.4 3.5 4.4 4.4l1.7-1.3 2.6 2.3-1.2 2.3C7 13.3 2.7 9 2.2 2.7z"/></svg>
          905-218-6937
        </li>
        <li>
          <svg viewBox="0 0 16 16" aria-hidden="true"><path d="M4 1h8v14H4zM5.5 2.5v9h5v-9zM7.2 12.6h1.6v1.2H7.2z" fill-rule="evenodd"/></svg>
          012-555-0148
        </li>
        <li>
          <svg viewBox="0 0 16 16" aria-hidden="true"><path d="M1 3.5h14v9H1zM2.5 4.5 8 9l5.5-4.5z" fill-rule="evenodd"/></svg>
          info@pollvarn.example
        </li>
        <li>
          <svg viewBox="0 0 16 16" aria-hidden="true"><path d="M8 1a7 7 0 1 0 0 14A7 7 0 0 0 8 1zm0 1.4c.8.8 1.4 2.2 1.6 3.9H6.4C6.6 4.6 7.2 3.2 8 2.4zM2.5 7.3h2.8c0 .5 0 1 .1 1.4H2.5a5.6 5.6 0 0 1 0-1.4zm4 0h3.1a9 9 0 0 1-.1 1.4H6.5a9 9 0 0 1 0-1.4zm4.2 0h2.8a5.6 5.6 0 0 1 0 1.4h-2.8zM6.4 9.7h3.2c-.2 1.7-.8 3.1-1.6 3.9-.8-.8-1.4-2.2-1.6-3.9z" fill-rule="evenodd"/></svg>
          www.pollvarn.example
        </li>
      </ul>
    </div>
  </section>

</main>
</body>
</html>
```